Financial investment & advisory business needs a powerpoint design

We need a powerpoint design incorporating the logo (and colours) and relating to the business card design we already have. The company is a boutique financial investment and advisory business called Torvane Hollis Pty Ltd based in Australia. The final design should communicate innovative advice and financial safety and growth. A young, contemporary but experienced, professional business.

Target Market(s)

Companies listed or wishing to list on the Kestrelvale Equities Bourse and Professional and Institutional Investors.

Industry/Entity Type

Finance

Requirements
Must have
• Incorporate the logo and colours. Be similar/relate to the business card design.
Nice to have
Should not have
• Do not deviate from the logo colours.
• Do not use black background or invert the logo.
• Do not deviate from the business card design too much.

```html
<!DOCTYPE html>
<html lang="en">
<head>
<meta charset="utf-8">
<title>Torvane Hollis – Presentation Template</title>
<link rel="stylesheet" href="https://fonts.googleapis.com/css2?family=Carlito:wght@400;700&family=Tinos&family=Arimo&display=swap">
<style>
  :root {
    --brand-blue: #3e62b0;
    --brand-sky: #4a8fce;
    --brand-grey: #8a8a8a;
    --ink: #3a3a3a;
    --paper: #ffffff;
    --stage: #0b0f1a;
    --slide-light: #fafafa;
    --slide-shade: #e2e2e2;
  }
  * { margin: 0; padding: 0; box-sizing: border-box; }
  html, body { width: 755px; height: 1200px; overflow: hidden; background: var(--stage); }
  body { position: relative; font-family: "Carlito", "Calibri", sans-serif; }

  .slide { position: absolute; left: 0; width: 755px; overflow: hidden; }

  /* ---------- Title slide ---------- */
  .title-slide { top: 0; height: 535px; background: var(--paper); }
  .accent-strip { position: absolute; top: 0; left: 0; width: 755px; height: 8px; display: flex; }
  .accent-strip span { flex: 1; }
  .accent-strip .a1 { background: var(--brand-blue); }
  .accent-strip .a2 { background: var(--brand-sky); }
  .accent-strip .a3 { background: var(--brand-grey); }

  .brand-mark {
    position: absolute; top: 88px; left: 0; width: 755px; text-align: center;
    font-size: 50px; font-weight: 400; letter-spacing: 2px; color: var(--brand-blue);
    font-variant: small-caps;
  }

  .hero-band { position: absolute; top: 226px; left: 0; width: 755px; height: 270px; }
  .hero-band svg { position: absolute; inset: 0; }
  .hero-title {
    position: absolute; left: 25px; top: 52px; width: 360px;
    color: var(--paper); font-weight: 700; font-size: 20.5px; line-height: 28px; text-transform: uppercase;
  }
  .hero-lede {
    position: absolute; left: 25px; top: 145px; width: 355px;
    color: var(--paper); font-size: 15.5px; line-height: 20px;
  }
  .meta { position: absolute; color: var(--paper); font-size: 15.5px; line-height: 20px; }
  .meta strong { text-transform: uppercase; }
  .meta-to { left: 486px; top: 42px; }
  .meta-by { left: 592px; top: 170px; }

  .contact-bar { position: absolute; top: 496px; left: 0; width: 755px; height: 39px; }
  .contact {
    position: absolute; top: 12px; display: flex; align-items: center; gap: 12px;
    font-family: "Tinos", "Georgia", serif; font-size: 12px; color: var(--ink);
  }
  .contact svg { width: 14px; height: 14px; fill: var(--brand-blue); }
  .contact-phone { left: 18px; }
  .contact-mail { left: 265px; }
  .contact-web { left: 565px; }

  /* ---------- Content slide ---------- */
  .content-slide {
    top: 557px; height: 533px;
    background: radial-gradient(ellipse at 45% 35%, var(--slide-light) 0%, #f0f0f0 50%, var(--slide-shade) 100%);
  }
  .slide-header { position: absolute; top: 0; left: 0; width: 755px; height: 43px; }
  .slide-header svg { position: absolute; inset: 0; }
  .slide-title {
    position: absolute; left: 18px; top: 9px; color: var(--paper);
    font-size: 21px; font-weight: 700; text-transform: uppercase;
  }
  .slide-number {
    position: absolute; right: 18px; top: 9px; color: var(--paper); font-weight: 700;
    font-size: 12px; text-transform: uppercase;
  }
  .slide-number b { font-size: 21px; margin-left: 4px; }

  .feature { position: absolute; width: 345px; text-align: center; }
  .feature-icon { display: block; margin: 0 auto 19px; width: 84px; height: 84px; }
  .feature-icon circle.ring { fill: none; stroke: var(--brand-blue); stroke-width: 2; }
  .feature-icon .glyph { fill: none; stroke: var(--brand-blue); stroke-width: 2; stroke-linecap: round; stroke-linejoin: round; }
  .feature p { font-size: 14.5px; line-height: 17.5px; color: var(--ink); }
  .f1 { left: 16px; top: 78px; }
  .f2 { left: 393px; top: 78px; }
  .f3 { left: 16px; top: 285px; }
  .f4 { left: 393px; top: 285px; }

  .slide-footer { position: absolute; left: 30px; top: 510px; width: 725px; border-top: 1px solid var(--brand-blue); }
  .slide-footer p { font-family: "Arimo", "Arial", sans-serif; font-size: 9.5px; color: var(--ink); padding-top: 4px; }

  /* ---------- Closing wordmark ---------- */
  .closing-mark {
    position: absolute; left: 30px; top: 1125px; color: var(--paper);
    font-size: 32px; letter-spacing: 1px; font-variant: small-caps;
  }
</style>
</head>
<body>

<section class="slide title-slide">
  <div class="accent-strip"><span class="a1"></span><span class="a2"></span><span class="a3"></span></div>
  <div class="brand-mark">Torvane Hollis</div>

  <div class="hero-band">
    <svg width="755" height="270" viewBox="0 0 755 270">
      <polygon points="0,0 466,0 370,270 0,270" fill="var(--brand-blue)"/>
      <polygon points="478,0 755,0 755,270 382,270" fill="var(--brand-sky)"/>
    </svg>
    <h1 class="hero-title">What you’re reading is the presentation title</h1>
    <p class="hero-lede">Lorem ipsum dolor sit amet, consectetur adipiscing elit. Vestibulum dolor elit, mattis non quam sed, sodales vestibulum justo.</p>
    <p class="meta meta-to">Presented to<br><strong>Company/Client Name</strong><br>24 Jun 2017</p>
    <p class="meta meta-by">Presented by<br><strong>Maren Ashcombe</strong><br>Office Manager</p>
  </div>

  <div class="contact-bar">
    <div class="contact contact-phone">
      <svg viewBox="0 0 24 24"><path d="M6.6 10.8c1.4 2.8 3.8 5.1 6.6 6.6l2.2-2.2c.3-.3.7-.4 1-.2 1.1.4 2.3.6 3.6.6.6 0 1 .4 1 1V20c0 .6-.4 1-1 1C10.6 21 3 13.4 3 4c0-.6.4-1 1-1h3.5c.6 0 1 .4 1 1 0 1.3.2 2.5.6 3.6.1.3 0 .7-.2 1z"/></svg>
      <span>+61 2 5550 0142</span>
    </div>
    <div class="contact contact-mail">
      <svg viewBox="0 0 24 24"><path d="M2 5h20v14H2z M3 6l9 7 9-7" fill="var(--brand-blue)"/><path d="M3 6.5l9 6.5 9-6.5" fill="none" stroke="#fff" stroke-width="1.6"/></svg>
      <span>info@torvanehollis.com.au</span>
    </div>
    <div class="contact contact-web">
      <svg viewBox="0 0 24 24"><circle cx="12" cy="12" r="10"/><path d="M2 12h20M12 2c3 3 3 17 0 20M12 2c-3 3-3 17 0 20" stroke="#fff" stroke-width="1.4" fill="none"/></svg>
      <span>www.torvanehollis.com.au</span>
    </div>
  </div>
</section>

<section class="slide content-slide">
  <header class="slide-header">
    <svg width="755" height="43" viewBox="0 0 755 43">
      <polygon points="0,0 676,0 634,43 0,43" fill="var(--brand-blue)"/>
      <polygon points="683,0 755,0 755,43 641,43" fill="var(--brand-sky)"/>
    </svg>
    <h2 class="slide-title">This is the slide title</h2>
    <div class="slide-number">Slide <b>02</b></div>
  </header>

  <article class="feature f1">
    <svg class="feature-icon" viewBox="0 0 84 84">
      <circle class="ring" cx="42" cy="42" r="40"/>
      <g class="glyph">
        <circle cx="49" cy="24" r="3.5"/>
        <path d="M37 34v8l-7 14h22l-7-14v-8"/>
        <path d="M34 34h14M33 49h16"/>
      </g>
    </svg>
    <p>Lorem ipsum dolor sit amet, consectetur adipiscing elit. Vestibulum dolor elit, mattis non quam sed, sodales vestibulum justo. Cras sed accumsan mi, in auctor nisi.</p>
  </article>

  <article class="feature f2">
    <svg class="feature-icon" viewBox="0 0 84 84">
      <circle class="ring" cx="42" cy="42" r="40"/>
      <g class="glyph">
        <circle cx="36" cy="47" r="5"/>
        <path d="M36 35v-3M36 62v-3M24 47h-3M51 47h-3M27.5 38.5l-2-2M46.5 57.5l-2-2M27.5 55.5l-2 2M46.5 36.5l-2 2"/>
        <circle cx="36" cy="47" r="10.5"/>
        <circle cx="56" cy="26" r="5"/>
        <path d="M56 18v-2M56 36v-2M48 26h-2M66 26h-2"/>
      </g>
    </svg>
    <p>Aenean mattis justo molestie, hendrerit velit eget, auctor est. Suspendisse mauris mi, pretium eu rhoncus nec, gravida ut lectus. Aliquam faucibus lorem ut rutrum tempor. Vivamus vulputate tempus velit.</p>
  </article>

  <article class="feature f3">
    <svg class="feature-icon" viewBox="0 0 84 84">
      <circle class="ring" cx="42" cy="42" r="40"/>
      <g class="glyph">
        <path d="M27 33h30l-3 26H30z"/>
        <path d="M35 33v-4a7 7 0 0 1 14 0v4"/>
        <path d="M45 40c-1-2-6-2-6 1s6 2 6 5-5 3-6 1M42 38v2M42 48v2"/>
      </g>
    </svg>
    <p>. In eleifend dui nunc, vel fringilla augue porttitor ac. Ut hendrerit erat et turpis dignissim ullamcorper. Suspendisse potenti. Nunc auctor lacus in elit vehicula, in facilisis arcu pretium.</p>
  </article>

  <article class="feature f4">
    <svg class="feature-icon" viewBox="0 0 84 84">
      <circle class="ring" cx="42" cy="42" r="40"/>
      <g class="glyph">
        <path d="M27 55a19 19 0 1 1 30 0"/>
        <path d="M42 46l3-14"/>
        <circle cx="42" cy="47" r="2"/>
      </g>
    </svg>
    <p>Suspendisse ut odio sit amet diam rhoncus pellentesque. Ut egestas ullamcorper massa, quis suscipit urna elementum quis. Interdum et malesuada fames ac ante ipsum primis in faucibus.</p>
  </article>

  <footer class="slide-footer"><p>Copyright 2017 © Torvane Hollis. All rights reserved.</p></footer>
</section>

<div class="closing-mark">Torvane Hollis</div>

</body>
</html>
```